Wine Bottle Label for Tall Fern Cellars

We are a small, newly established winery in need of an original, bold and outstanding bottle label design for our Tall Fern wine.

Our vineyard and winery are located on a 200 acre farm in a remote part of southern Oregon. The name "Tall Fern" was inspired by the large, overgrown size of all of the foliage here, including our grapevines. Things grow large and vigorous in Oregon! And everything is very lush and green. It is almost surreal or other-worldly, like the landscapes seen in the Keeper of The Hollows movies, or the land of Yarrowmere. It is a place that makes you say "wow" with its epic, large scale, natural beauty.

The name "Tall Fern" also captures the essence of our wine. It is big in flavor, quality and color. Our first release is a Pinot Noir (red). Pinot Noir wines often are subtle in flavor and thin in their color. Our label should convey that our Pinot Noir is a much more robust, darker, heavier, meatier, more flavorful wine that is a lot more fun than an "ordinary" wine. At the same time, this wine is not cheap, and so nothing in the label should convey "bargain," "low price," or "cheapness." This is a fine wine with a sense of adventure. Be sure to convey "quality" with your design along with "big," "adventure" and "fun".

The label should appeal to a younger demographic, both male and female, between the ages of 21 and 35. It should be non-traditional and adventurous and suggest a pushing of boundaries and a breaking of rules. This Pinot Noir does not conform to the normal "limitations" of the variety, therefore the label should not conform. It should have an "organic" or "natural" or "agricultural" vibe, as opposed to something mechanical or technical. It should, however, be contemporary. Do not confuse "natural" or "organic" with being nostalgic or old school. Think "agri-hipsters."

The label should be designed to fit on a Burgundy-style wine bottle (photo attached for reference). (Note: All Pinot Noir and Chardonnay is bottled in Burgundy bottles, If you are not sure about the bottle shape you can go to a local store and compare the various bottles. Locate a bottle of Pinot Noir or Chardonnay or anything identified as a "Burgundy Wine," and it should be the correct bottle. The tall, skinny bottles used for Cabernet Sauvignon are NOT correct)). Please see the "Must Have" notes for more on the bottle.

In summary, the final project should be a wine bottle label design that conveys bigness, vastness, adventurous, non-traditional, high quality wine. A good tagline to keep in mind is "Living Large."

Target Market(s)

Young, hip, non-conformist wine drinkers aged 21-35 with a sense of adventure and an appreciation of quality.

Industry/Entity Type

School

Requirements
Must have
• *Must contain the words:

Tall Fern (the brand)
2013 Pinot Noir (the vintage year and variety)

*The label must be designed to fit a Burgundy-style wine bottle. A photo is attached for reference.

*Additionally, the label needs to fit on the lower, widest part of the bottle. The label will be printed on sticky paper and rolled onto the bottle with a machine. The machine cannot apply labels to the neck of the bottle. The maximum size of a label that will fit this space is 5.5 inches wide by 4.5 inches tall. You DO NOT have to fill ALL of this space or confine the label shape to a rectangle, but the label cannot exceed this size or it won't stick to the bottle properly. It will really help if you can put your hands on an actual bottle to see the logistics of applying the label. But if that is not possible, just do your best with the instructions you have. I am confident the winning design could be adjusted to fit the bottle, if necessary
Nice to have
• *Wine grape leaf or leaves.

*A concept I have been playing with is sunlight shining through leaves like light through a Kessler lamp or a stained glass window. This is NOT a requirement for this label. However, if the concept inspires and idea, I would be most happy to see it.
Should not have
• IF a leaf or leaves are included in the design (not a requirement) they MUST be wine grapevine leafs and preferably leaves of the Pinot Noir vine. Do not use generic leaves or identifiable leaves such as oak leaves, maple leaves, or anything that looks like the Canadian flag or the Dunmore Ice Hawks hockey logo. Reference the attached photos of wine grape leaves to see the correct leaf type. I am happy to email more photos upon request. These photos may be used in whole or in part in your design, however, a leaf from a photo is NOT a requirement, nor is the image of a leaf or leaves.

This label should NOT be designed for Bordeaux-style wine bottles (the tall, skinny ones).

```html
<!DOCTYPE html>
<html lang="en">
<head>
<meta charset="utf-8">
<title>Tall Fern 2013 Pinot Noir Label</title>
<link rel="stylesheet" href="https://fonts.googleapis.com/css2?family=Fredoka:wght@500;600&display=swap">
<style>
  :root {
    --page-bg: #ffffff;
    --leaf-light: #7fae3c;
    --leaf-mid: #4f8a2a;
    --leaf-deep: #2c5a1c;
    --label-text: #ffffff;
    --text-shadow: rgba(20, 50, 10, 0.35);
  }
  * { margin: 0; padding: 0; box-sizing: border-box; }
  html, body {
    width: 900px;
    height: 1200px;
    overflow: hidden;
    background: var(--page-bg);
  }
  .canvas {
    position: relative;
    width: 900px;
    height: 1200px;
  }
  .wine-label {
    position: absolute;
    left: 65px;
    top: 285px;
    width: 770px;
    height: 630px;
  }
  .leaf-artwork {
    position: absolute;
    inset: 0;
    width: 100%;
    height: 100%;
  }
  .label-type {
    position: absolute;
    inset: 0;
    font-family: "Fredoka", sans-serif;
    color: var(--label-text);
    text-shadow: 0 2px 6px var(--text-shadow);
  }
  .brand-word {
    position: absolute;
    font-weight: 600;
    font-size: 168px;
    line-height: 1;
    letter-spacing: 2px;
  }
  .brand-word--first { left: 120px; top: 95px; }
  .brand-word--second { left: 235px; top: 245px; }
  .vintage-year {
    position: absolute;
    left: 178px;
    top: 330px;
    font-weight: 500;
    font-size: 68px;
    line-height: 1;
    transform: rotate(90deg);
    transform-origin: left top;
  }
  .variety {
    position: absolute;
    left: 240px;
    top: 425px;
    font-weight: 500;
    font-size: 74px;
    line-height: 1;
  }
</style>
</head>
<body>
<main class="canvas">
  <section class="wine-label">
    <svg class="leaf-artwork" viewBox="0 0 770 630" role="img" aria-label="Backlit green grapevine leaf photograph forming the label shape">
      <defs>
        <radialGradient id="leafGlow" cx="45%" cy="40%" r="75%">
          <stop offset="0%" stop-color="var(--leaf-light)"/>
          <stop offset="55%" stop-color="var(--leaf-mid)"/>
          <stop offset="100%" stop-color="var(--leaf-deep)"/>
        </radialGradient>
      </defs>
      <path d="M40 70 Q120 20 230 40 Q330 5 430 30 Q540 0 640 40 Q740 60 750 160 Q770 260 740 360 Q765 470 700 560 Q600 630 470 600 Q370 625 270 600 Q150 625 70 560 Q10 470 30 360 Q5 250 25 160 Q20 100 40 70 Z" fill="url(#leafGlow)"/>
    </svg>
    <div class="label-type">
      <span class="brand-word brand-word--first">TALL</span>
      <span class="brand-word brand-word--second">FERN</span>
      <span class="vintage-year">2013</span>
      <span class="variety">Pinot Noir</span>
    </div>
  </section>
</main>
</body>
</html>
```